Book cover for ebook and Physical book for Mind Clutter Collective

I run a non-profit Mind Clutter Collective and I have a new book that needs a cover. For the physical book, I will need a full wrap. The mission is to help individuals Escape the cycle of restless inner chatter. This book is title is "Escape the cycle of restless inner chatter", and subtitle "Release Your Mind from Clutter." I am open to anything design wise, nothing is set in stone. Oh, MCC is pending Trademark.

Target Market(s)

Typically it's Mom's from 25-40

Industry/Entity Type

Mental Health

Font styles to use
Serif

Colors
f37122
9bcb3b
fbed22
0255a3
e34197

Requirements
Must have
• I do like simplicity, yet vibrant colors.
Nice to have
• The authors are Neil R. Dawkins, and Vera Holmquist. For some inspiration individuals refer to me as the Wonder Healer having reversed five incurable diseases.
Should not have
• The cover shouldn't be too busy.

```html
<!DOCTYPE html>
<html lang="en">
<head>
<meta charset="utf-8">
<title>Escape the Cycle of Restless Inner Chatter — Book Cover</title>
<link rel="stylesheet" href="https://fonts.googleapis.com/css2?family=Anton&family=Archivo+Black&family=Jost:wght@400&display=swap">
<style>
  :root {
    --ink: #231f20;
    --orange: #f37122;
    --green: #9bcb3b;
    --white: #ffffff;
    --photo-grey-1: #d9d9d9;
    --photo-grey-2: #9e9e9e;
    --photo-blue-1: #b9dcf2;
    --photo-blue-2: #e9c9b0;
  }
  html, body {
    margin: 0;
    padding: 0;
    width: 800px;
    height: 1200px;
    overflow: hidden;
    background: var(--white);
  }
  .cover {
    position: relative;
    width: 800px;
    height: 1200px;
    overflow: hidden;
  }
  .band-title {
    position: absolute;
    left: 0; top: 0;
    width: 800px; height: 604px;
    background: var(--ink);
  }
  .band-subtitle {
    position: absolute;
    left: 0; top: 604px;
    width: 800px; height: 525px;
    background: var(--green);
  }
  .band-authors {
    position: absolute;
    left: 0; top: 1129px;
    width: 800px; height: 71px;
    background: var(--white);
  }
  .portrait-frown {
    position: absolute;
    left: 0; top: 14px;
    width: 318px; height: 590px;
    background: linear-gradient(180deg, var(--photo-blue-2) 0%, var(--photo-grey-1) 40%, var(--photo-grey-2) 100%);
    border-radius: 140px 140px 0 0;
  }
  .portrait-joy {
    position: absolute;
    left: 370px; top: 614px;
    width: 362px; height: 515px;
    background: linear-gradient(180deg, var(--photo-blue-2) 0%, var(--photo-blue-1) 45%, #8fc3e6 100%);
    border-radius: 150px 150px 0 0;
  }
  .type-layer {
    position: absolute;
    left: 0; top: 0;
  }
  .display {
    font-family: "Anton", "Impact", sans-serif;
  }
  .connector {
    font-family: "Archivo Black", "Arial Black", sans-serif;
  }
  .authors {
    font-family: "Jost", "Futura", sans-serif;
    font-size: 31px;
    fill: var(--orange);
  }
  .fill-orange { fill: var(--orange); }
  .fill-white { fill: var(--white); }
  .fill-ink { fill: var(--ink); }
</style>
</head>
<body>
<main class="cover">
  <div class="band-title"></div>
  <div class="band-subtitle"></div>
  <div class="band-authors"></div>

  <div class="portrait-frown" role="img" aria-label="Photo of a short-haired woman in a grey T-shirt with a doubtful, frowning expression"></div>
  <div class="portrait-joy" role="img" aria-label="Photo of the same woman in a light blue T-shirt, smiling widely with both hands raised in joy"></div>

  <svg class="type-layer" width="800" height="1200" viewBox="0 0 800 1200">
    <g class="title">
      <text class="display fill-orange" x="347" y="144" font-size="150" textLength="433" lengthAdjust="spacingAndGlyphs">ESCAPE</text>
      <text class="connector fill-white" x="378" y="238" font-size="84" textLength="344" lengthAdjust="spacingAndGlyphs">the Cycle</text>
      <text class="display fill-orange" x="318" y="364" font-size="112" textLength="468" lengthAdjust="spacingAndGlyphs">OF RESTLESS</text>
      <text class="display fill-orange" x="372" y="480" font-size="112" textLength="350" lengthAdjust="spacingAndGlyphs">INNER</text>
      <text class="display fill-orange" x="340" y="594" font-size="112" textLength="421" lengthAdjust="spacingAndGlyphs">CHATTER</text>
    </g>
    <g class="subtitle">
      <text class="display fill-orange" x="98" y="769" font-size="74" textLength="200" lengthAdjust="spacingAndGlyphs">RELEASE</text>
      <text class="display fill-ink" x="76" y="852" font-size="70" textLength="244" lengthAdjust="spacingAndGlyphs">YOUR MIND</text>
      <text class="display fill-ink" x="129" y="935" font-size="70" textLength="138" lengthAdjust="spacingAndGlyphs">FROM</text>
      <text class="display fill-orange" x="52" y="1018" font-size="70" textLength="302" lengthAdjust="spacingAndGlyphs">CLUTTER</text>
    </g>
    <text class="authors" x="388" y="1175" text-anchor="middle" xml:space="preserve">Neil R. Dawkins  and  Vera Holmquist</text>
  </svg>
</main>
</body>
</html>
```